Design a Website Mockup - HOMEPAGE ONLY - Brixley Mortgage

Need a new design for the HOMEPAGE only for Brixley Mortgage. Looking for something fresh and modern. Need ASAP.

You can view the original website here - [url removed, login to view]

VERY IMPORTANT - Do not contact any person from the existing website.

```html
<!DOCTYPE html>
<html lang="en">
<head>
<meta charset="utf-8">
<title>Brixley Mortgage – Home Loan</title>
<link rel="stylesheet" href="https://fonts.googleapis.com/css2?family=Oswald:wght@400;500;700&family=Open+Sans:wght@400;600;700&display=swap">
<style>
:root{
  --blue:#2eaee6;
  --blue-dark:#1f8fc2;
  --ink:#333333;
  --ink-soft:#666666;
  --pale:#eaf6fc;
  --white:#ffffff;
  --btn:#2b2b2b;
  --photo-a:#8a7a6a;
  --photo-b:#c9b8a3;
  --sky-a:#9fb7c9;
  --sky-b:#d9d3c6;
}
*{box-sizing:border-box;margin:0;padding:0}
html,body{width:1200px;height:2441px;overflow:hidden;background:var(--white)}
body{font-family:"Open Sans",Arial,sans-serif;color:var(--ink);position:relative}
.wrap{width:760px;margin:0 auto;position:relative}
.heading{font-family:"Oswald",Arial,sans-serif}

/* top bar */
.topbar{height:56px;background:var(--white)}
.topbar .wrap{display:flex;justify-content:space-between;align-items:center;height:56px;width:820px}
.brand{font-family:"Oswald",Arial,sans-serif;font-weight:500;font-size:26px;color:var(--blue)}
.topbar-offer{font-family:"Oswald",Arial,sans-serif;font-size:22px;color:var(--ink)}
.topbar-offer span{color:var(--blue)}

/* hero */
.hero{height:474px;position:relative;background:linear-gradient(100deg,#5a6b73 0%,var(--photo-a) 40%,#b9c4c2 70%,#e3e6df 100%)}
.hero-copy{position:absolute;left:220px;top:70px;color:var(--white)}
.hero-title{font-family:"Oswald",Arial,sans-serif;font-weight:700;font-size:92px;line-height:1;letter-spacing:1px}
.hero-sub{font-family:"Oswald",Arial,sans-serif;font-weight:500;font-size:40px;margin-top:6px}
.apply-form{position:absolute;left:740px;top:56px;width:222px;height:322px;background:var(--blue);padding:16px 18px}
.apply-form h2{font-family:"Oswald",Arial,sans-serif;font-weight:500;color:var(--white);font-size:36px;text-align:center;line-height:1.1;margin-bottom:14px}
.field{height:30px;background:var(--white);margin-bottom:10px;font-size:12px;color:#888;padding:7px 10px}
.btn{display:inline-block;background:var(--btn);color:var(--white);font-family:"Oswald",Arial,sans-serif;font-size:18px;letter-spacing:1px;text-align:center}
.apply-form .btn{width:100%;height:42px;line-height:42px;margin-top:12px}

/* deals */
.deals{height:305px;background:var(--pale);padding-top:40px}
.deals-title{text-align:center;font-family:"Oswald",Arial,sans-serif;font-weight:500;color:var(--blue);font-size:30px;line-height:1.1}
.deals-rate{text-align:center;font-family:"Oswald",Arial,sans-serif;font-size:28px;color:var(--ink)}
.features{display:flex;justify-content:space-between;margin-top:28px}
.feature{width:220px}
.feature-head{display:flex;align-items:center;gap:10px}
.feature-head svg{flex:none}
.feature-name{font-family:"Oswald",Arial,sans-serif;color:var(--blue);font-weight:500;font-size:22px;line-height:1}
.feature-sub{font-size:13px;color:var(--ink)}
.feature p{font-size:12px;line-height:1.6;color:var(--ink-soft);margin-top:14px}

/* split sections */
.split{height:385px;position:relative}
.photo{position:absolute;display:block}
.split-text{position:absolute;width:340px}
.kicker{font-family:"Oswald",Arial,sans-serif;font-weight:500;color:var(--blue);font-size:34px;line-height:1.1}
.sub-title{font-family:"Oswald",Arial,sans-serif;font-size:32px;color:var(--ink);line-height:1.15}
.split-text p{font-size:12.5px;line-height:1.6;color:var(--ink-soft);margin:14px 0 20px}
.split-text .btn{width:118px;height:44px;line-height:44px;font-size:16px}

/* testimonials */
.testimonials{height:305px;background:var(--blue);padding-top:52px}
.testimonials .wrap{display:flex;justify-content:space-between}
.quote{width:220px;text-align:center;color:var(--white)}
.avatar{width:50px;height:50px;border-radius:50%;background:linear-gradient(160deg,#d8c1a8,#8a6e58);border:3px solid var(--white);margin:0 auto 14px}
.quote p{font-size:12px;line-height:1.6}
.quote .name{font-family:"Oswald",Arial,sans-serif;font-size:15px;letter-spacing:1px;margin-top:14px}

/* news */
.news{height:470px;background:var(--pale);padding-top:40px}
.news-title{text-align:center;font-family:"Oswald",Arial,sans-serif;font-weight:500;color:var(--blue);font-size:36px;line-height:1.1}
.news-sub{text-align:center;font-family:"Oswald",Arial,sans-serif;font-size:34px;color:var(--ink)}
.news-grid{display:flex;justify-content:space-between;margin-top:26px}
.news-item{width:228px}
.news-img{height:190px;background:linear-gradient(170deg,var(--sky-a),var(--sky-b) 55%,#8f9a6e)}
.news-cap{font-family:"Oswald",Arial,sans-serif;font-weight:500;color:var(--blue);font-size:20px;margin-top:14px;line-height:1.1}
.news-cap2{font-family:"Oswald",Arial,sans-serif;font-size:20px;color:var(--ink)}

/* footer */
.footer{height:61px;background:var(--blue);color:var(--white);text-align:center;font-size:12px;line-height:61px}
</style>
</head>
<body>

<header class="topbar">
  <div class="wrap">
    <div class="brand">Brixley Mortgage</div>
    <div class="topbar-offer">Apply for a Home Loan <span>@9.95%</span></div>
  </div>
</header>

<section class="hero" role="img" aria-label="Photo of a smiling couple in front of their new house">
  <div class="hero-copy">
    <div class="hero-title">BIG DREAMS</div>
    <div class="hero-sub">Even Bigger and Better Loans</div>
  </div>
  <form class="apply-form">
    <h2>APPLY NOW</h2>
    <div class="field">Full Name</div>
    <div class="field">Email Address</div>
    <div class="field">Phone Number</div>
    <div class="field">Loan Amount</div>
    <div class="btn">CONTINUE</div>
  </form>
</section>

<section class="deals">
  <div class="deals-title">BEST DEALS FOR HOME LOAN</div>
  <div class="deals-rate">Interest Rate @9.95%</div>
  <div class="wrap features">
    <div class="feature">
      <div class="feature-head">
        <svg width="40" height="40" viewBox="0 0 40 40"><circle cx="20" cy="20" r="20" fill="var(--blue)"/><path d="M11 20.5l6 6 12-13" fill="none" stroke="#fff" stroke-width="4" stroke-linecap="round" stroke-linejoin="round"/></svg>
        <div><div class="feature-name">NO DOWN</div><div class="feature-sub">Payment Required</div></div>
      </div>
      <p>Lorem Ipsum is simply dummy text of the printing and typesetting industry, standard dummy text ever.</p>
    </div>
    <div class="feature">
      <div class="feature-head">
        <svg width="40" height="40" viewBox="0 0 40 40"><circle cx="20" cy="20" r="20" fill="var(--blue)"/><path d="M11 20.5l6 6 12-13" fill="none" stroke="#fff" stroke-width="4" stroke-linecap="round" stroke-linejoin="round"/></svg>
        <div><div class="feature-name">LOWER</div><div class="feature-sub">Interest Rates</div></div>
      </div>
      <p>Lorem Ipsum is simply dummy text of the printing and typesetting industry, standard dummy text ever.</p>
    </div>
    <div class="feature">
      <div class="feature-head">
        <svg width="40" height="40" viewBox="0 0 40 40"><circle cx="20" cy="20" r="20" fill="var(--blue)"/><path d="M11 20.5l6 6 12-13" fill="none" stroke="#fff" stroke-width="4" stroke-linecap="round" stroke-linejoin="round"/></svg>
        <div><div class="feature-name">EASY</div><div class="feature-sub">Qualification</div></div>
      </div>
      <p>Lorem Ipsum is simply dummy text of the printing and typesetting industry, standard dummy text ever.</p>
    </div>
  </div>
</section>

<section class="split">
  <div class="photo" role="img" aria-label="Photo of a family sitting on the front steps of their home" style="left:225px;top:0;width:362px;height:360px;background:linear-gradient(160deg,#7d5a48,var(--photo-b) 60%,#a58d78)"></div>
  <div class="split-text" style="left:612px;top:40px">
    <div class="kicker">PROFESSIONAL</div>
    <div class="sub-title">Home Loan Services</div>
    <p>It is a long established fact that a reader will be distracted by the readable content of a page when looking at its layout. The point of using Lorem Ipsum is that it has a more-or-less normal distribution of letters.</p>
    <div class="btn">APPLY NOW</div>
  </div>
</section>

<section class="testimonials">
  <div class="wrap">
    <div class="quote">
      <div class="avatar" role="img" aria-label="Customer portrait"></div>
      <p>It is a long established fact that a reader will be distracted by the readable content of a page when looking at its layout and design.</p>
      <div class="name">JORDAN REEVE</div>
    </div>
    <div class="quote">
      <div class="avatar" role="img" aria-label="Customer portrait"></div>
      <p>It is a long established fact that a reader will be distracted by the readable content of a page when looking at its layout and design.</p>
      <div class="name">SANDRA COOPER</div>
    </div>
    <div class="quote">
      <div class="avatar" role="img" aria-label="Customer portrait"></div>
      <p>It is a long established fact that a reader will be distracted by the readable content of a page when looking at its layout and design.</p>
      <div class="name">FELIX LANE</div>
    </div>
  </div>
</section>

<section class="split">
  <div class="split-text" style="left:225px;top:40px">
    <div class="kicker">YOUR DREAM HOME</div>
    <div class="sub-title">Is a Click Away</div>
    <p>It is a long established fact that a reader will be distracted by the readable content of a page when looking at its layout. The point of using Lorem Ipsum is that it has a more-or-less normal distribution of letters.</p>
    <div class="btn">APPLY NOW</div>
  </div>
  <div class="photo" role="img" aria-label="Photo of a mother and children in front of a house with a flag" style="left:590px;top:20px;width:390px;height:345px;background:linear-gradient(170deg,var(--sky-a),var(--sky-b) 50%,#b06a5a)"></div>
</section>

<section class="news">
  <div class="news-title">LATEST NEWS</div>
  <div class="news-sub">Lorem Ipsum is simply dummy text</div>
  <div class="wrap news-grid">
    <div class="news-item">
      <div class="news-img" role="img" aria-label="Photo of a family outside a suburban house"></div>
      <div class="news-cap">THERE ARE MANY</div>
      <div class="news-cap2">Variations of Passages</div>
    </div>
    <div class="news-item">
      <div class="news-img" role="img" aria-label="Photo of a family on the lawn of their home"></div>
      <div class="news-cap">THERE ARE MANY</div>
      <div class="news-cap2">Variations of Passages</div>
    </div>
    <div class="news-item">
      <div class="news-img" role="img" aria-label="Photo of a couple in front of a new house"></div>
      <div class="news-cap">THERE ARE MANY</div>
      <div class="news-cap2">Variations of Passages</div>
    </div>
  </div>
</section>

<footer class="footer">Copyright © 2024 All Rights Reserved | www.brixleymortgage.com</footer>

</body>
</html>
```